Waschkarten-Design für Tankstelle gesucht
Zielgruppe
Unsere Tankstelle hat in eine neue Waschanlage investiert. Die Alten Waschkarten gefallen nicht mehr, und sind auch mit der Programmstruktur nicht mehr kompatibel. Siehe Anhang.
Waschkunden in der Portalwaschanlage jeglichen Alters und Geschlechts.
Aufgabenstellung
Wertigkeit der einzelnen Waschprogramme muss erkennbar sein. Beschriftung z. B. Mehrfachwäschen 3er 5er 10er bzw. Wertkarten der Preis soll veränderbar sein, so das die Karten jederzeit angepasst werden können. Auch sollte der Programm-Name von uns selbst geändert werden können. Die Einschiebe Richtung muss klar erkennbar sein.
Das Design muss im Check-Kartenformat sein. Achtung abgerundete Ecken mit ca. r=2 mm
Anbei ein Bild von unserer Neuen Waschanlage

```html
<!DOCTYPE html>
<html lang="de">
<head>
<meta charset="utf-8">
<title>Waschkarten Premium und Express</title>
<link rel="stylesheet" href="https://fonts.googleapis.com/css2?family=Open+Sans:wght@400;700;800&display=swap">
<style>
  :root {
    --frame: #0d4a5a;
    --paper: #ffffff;
    --band-white: #fdfdfc;
    --price-grey: #8e8e8e;
    --logo-ink: #111111;
    --pale-yellow: #f6eeaa;
    --premium-left: #f0b92c;
    --premium-band: #f0a62a;
    --express-left: #97bf87;
    --express-band: #48b0b0;
    --text-white: #ffffff;
  }
  html, body {
    margin: 0;
    width: 1200px;
    height: 1200px;
    overflow: hidden;
    background: var(--paper);
  }
  .canvas {
    position: relative;
    width: 1200px;
    height: 1200px;
    box-sizing: border-box;
    border: 6px solid var(--frame);
    background: var(--paper);
    font-family: "Open Sans", sans-serif;
  }
  .wash-card {
    position: absolute;
    left: 293px;
    width: 602px;
    height: 383px;
    display: block;
  }
  .wash-card--premium { top: 187px; }
  .wash-card--express { top: 618px; }
  .card-title { font-family: "Open Sans", sans-serif; font-weight: 800; }
  .card-price { font-family: "Open Sans", sans-serif; font-weight: 700; font-size: 46px; fill: var(--price-grey); }
  .card-program { font-family: "Open Sans", sans-serif; font-weight: 400; font-size: 27px; fill: var(--text-white); }
  .station-name { font-family: "Open Sans", sans-serif; font-weight: 700; fill: var(--logo-ink); }
</style>
</head>
<body>
<main class="canvas">

  <svg class="wash-card wash-card--premium" viewBox="0 0 602 383" xmlns="http://www.w3.org/2000/svg">
    <defs>
      <linearGradient id="premium-photo" x1="0" y1="0" x2="1" y2="0">
        <stop offset="0" stop-color="#e9e2a2"/>
        <stop offset="0.12" stop-color="#55585a"/>
        <stop offset="0.32" stop-color="#2f3336"/>
        <stop offset="0.5" stop-color="#6e8fb2"/>
        <stop offset="0.75" stop-color="#e2e8ee"/>
        <stop offset="1" stop-color="#7891ab"/>
      </linearGradient>
      <linearGradient id="premium-gold" x1="0" y1="0" x2="0" y2="1">
        <stop offset="0" stop-color="#c79a3a"/>
        <stop offset="0.35" stop-color="#f3dc9c"/>
        <stop offset="0.7" stop-color="#d9a640"/>
        <stop offset="1" stop-color="#b9882c"/>
      </linearGradient>
      <filter id="premium-shadow" x="-10%" y="-20%" width="130%" height="150%">
        <feDropShadow dx="4" dy="5" stdDeviation="4" flood-color="#000" flood-opacity="0.5"/>
      </filter>
      <filter id="premium-band-shadow" x="-5%" y="-20%" width="110%" height="140%">
        <feDropShadow dx="0" dy="-2" stdDeviation="3" flood-color="#000" flood-opacity="0.35"/>
      </filter>
    </defs>
    <rect class="card-photo" x="0" y="0" width="602" height="287" fill="url(#premium-photo)" role="img" aria-label="Foto der Portalwaschanlage mit Bürsten vor bewölktem Himmel"/>
    <rect class="card-corner" x="0" y="275" width="170" height="108" fill="var(--premium-left)"/>
    <g class="price-band" filter="url(#premium-band-shadow)">
      <rect x="157" y="201" width="445" height="86" fill="var(--band-white)"/>
      <path d="M157 201 L205 201 Q170 240 160 287 L157 287 Z" fill="var(--pale-yellow)"/>
    </g>
    <path class="program-band" d="M160 287 L602 287 L602 383 L133 383 Q140 320 160 287 Z" fill="var(--premium-band)" filter="url(#premium-band-shadow)"/>
    <text class="card-title" x="51" y="162" font-size="110" textLength="507" lengthAdjust="spacingAndGlyphs" fill="url(#premium-gold)" filter="url(#premium-shadow)">PREMIUM</text>
    <text class="station-name" x="282" y="225" font-size="11" text-anchor="middle">Tankstelle</text>
    <text class="station-name" x="282" y="260" font-size="26" text-anchor="middle">Lindner</text>
    <text class="card-price" x="563" y="262" text-anchor="end">€ 16,95</text>
    <text class="card-program" x="563" y="335" text-anchor="end">POLITURPROGRAMM &amp;</text>
    <text class="card-program" x="563" y="363" text-anchor="end">UNTERBODENWÄSCHE</text>
  </svg>

  <svg class="wash-card wash-card--express" viewBox="0 0 602 383" xmlns="http://www.w3.org/2000/svg">
    <defs>
      <linearGradient id="express-photo" x1="0" y1="0" x2="1" y2="0">
        <stop offset="0" stop-color="#e9e2a2"/>
        <stop offset="0.12" stop-color="#55585a"/>
        <stop offset="0.32" stop-color="#2f3336"/>
        <stop offset="0.5" stop-color="#6e8fb2"/>
        <stop offset="0.75" stop-color="#e2e8ee"/>
        <stop offset="1" stop-color="#7891ab"/>
      </linearGradient>
      <linearGradient id="express-teal" x1="0" y1="0" x2="1" y2="0">
        <stop offset="0" stop-color="#3ea7a6"/>
        <stop offset="0.5" stop-color="#7cbf8e"/>
        <stop offset="1" stop-color="#46aaa8"/>
      </linearGradient>
      <filter id="express-shadow" x="-10%" y="-20%" width="130%" height="150%">
        <feDropShadow dx="4" dy="5" stdDeviation="4" flood-color="#000" flood-opacity="0.5"/>
      </filter>
      <filter id="express-band-shadow" x="-5%" y="-20%" width="110%" height="140%">
        <feDropShadow dx="0" dy="-2" stdDeviation="3" flood-color="#000" flood-opacity="0.35"/>
      </filter>
    </defs>
    <rect class="card-photo" x="0" y="0" width="602" height="287" fill="url(#express-photo)" role="img" aria-label="Foto der Portalwaschanlage mit Bürsten vor bewölktem Himmel"/>
    <rect class="card-corner" x="0" y="275" width="170" height="108" fill="var(--express-left)"/>
    <g class="price-band" filter="url(#express-band-shadow)">
      <rect x="157" y="201" width="445" height="86" fill="var(--band-white)"/>
      <path d="M157 201 L205 201 Q170 240 160 287 L157 287 Z" fill="var(--pale-yellow)"/>
    </g>
    <path class="program-band" d="M160 287 L602 287 L602 383 L133 383 Q140 320 160 287 Z" fill="var(--express-band)" filter="url(#express-band-shadow)"/>
    <text class="card-title" x="74" y="161" font-size="108" textLength="459" lengthAdjust="spacingAndGlyphs" fill="url(#express-teal)" filter="url(#express-shadow)">EXPRESS</text>
    <text class="station-name" x="282" y="225" font-size="11" text-anchor="middle">Tankstelle</text>
    <text class="station-name" x="282" y="260" font-size="26" text-anchor="middle">Lindner</text>
    <text class="card-price" x="563" y="262" text-anchor="end">€ 5,95</text>
    <text class="card-program" x="563" y="334" text-anchor="end">Waschen &amp; Trocknen</text>
  </svg>

</main>
</body>
</html>
```